Business Card Design

Its a residential construction company

Industry/Entity Type

Residential

Contact Information for Business Card

Belvora Homes Pty Ltd,
Dylan R Foster
BE (Civil), Grad.Dip Hwy, Eng. (QCTU), FTC.Aust,
Director, Belvora Homes Pty Ltd

PO Box 587, Harlow Creek, VIC, 3942. Tel: 048765 2231
email: dylan@belvorahomes.com

```html
<!DOCTYPE html>
<html lang="en">
<head>
<meta charset="utf-8">
<title>Belvora Homes Pty Ltd — Business Card</title>
<link href="https://fonts.googleapis.com/css2?family=Tinos:wght@400;700&display=swap" rel="stylesheet">
<style>
  :root {
    --brand-blue: #1f3f95;
    --brand-red: #e0353f;
    --card-white: #fbfbfb;
    --stage: #e9e7e3;
    --text-font: "Tinos", "Times New Roman", serif;
  }
  * { box-sizing: border-box; margin: 0; padding: 0; }
  html, body {
    width: 1200px; height: 892px; overflow: hidden;
    background: var(--stage);
    font-family: var(--text-font);
  }
  .business-card {
    position: absolute; left: 100px; top: 160px;
    width: 1000px; height: 572px;
    background: var(--card-white);
    box-shadow: 0 6px 24px rgba(0,0,0,0.12);
  }
  .brand-block {
    position: absolute; left: 0; top: 0; width: 520px; height: 100%;
    display: flex; align-items: center; justify-content: center; gap: 20px;
  }
  .brand-mark {
    width: 44px; height: 44px; background: var(--brand-red); flex: none;
  }
  .brand-name {
    color: var(--brand-blue); font-weight: 700; font-size: 50px;
    line-height: 1.05; width: 330px;
  }
  .divider {
    position: absolute; left: 520px; top: 90px;
    width: 2px; height: 392px; background: var(--brand-blue);
  }
  .contact-block {
    position: absolute; left: 570px; top: 120px; width: 410px;
    color: var(--brand-blue);
  }
  .person-name {
    color: var(--brand-red); font-size: 40px; font-weight: 400; line-height: 1;
  }
  .person-role, .person-credentials {
    font-size: 19px; line-height: 1.2;
  }
  .person-role { margin-top: 10px; }
  .contact-list { list-style: none; margin-top: 42px; }
  .contact-item {
    display: flex; align-items: center; gap: 16px;
    font-size: 24px; line-height: 1; margin-bottom: 16px;
    white-space: nowrap;
  }
  .contact-icon {
    width: 24px; height: 24px; flex: none;
    background: var(--brand-red); border-radius: 5px;
    display: flex; align-items: center; justify-content: center;
  }
  .contact-icon svg { width: 16px; height: 16px; }
</style>
</head>
<body>
  <section class="business-card">
    <div class="brand-block">
      <span class="brand-mark"></span>
      <span class="brand-name">Belvora Homes Pty Ltd</span>
    </div>

    <div class="divider"></div>

    <div class="contact-block">
      <h1 class="person-name">Dylan R Foster</h1>
      <p class="person-role">Director</p>
      <p class="person-credentials">BE (Civil), Grad.Dip Hwy, Eng. (QCTU),<br>FTC.Aust</p>

      <ul class="contact-list">
        <li class="contact-item">
          <span class="contact-icon">
            <svg viewBox="0 0 16 16" aria-hidden="true"><path fill="#fff" d="M4 2l2.5 3-1.5 1.5c.8 1.8 2.2 3.2 4 4L10.5 9 13.5 11.5 12 14C7 13.5 2.5 9 2 4z"/></svg>
          </span>
          048765 2231
        </li>
        <li class="contact-item">
          <span class="contact-icon">
            <svg viewBox="0 0 16 16" aria-hidden="true"><rect x="2" y="4" width="12" height="8" fill="none" stroke="#fff" stroke-width="1.5"/><path d="M2 4l6 5 6-5" fill="none" stroke="#fff" stroke-width="1.5"/></svg>
          </span>
          dylan@belvorahomes.com
        </li>
        <li class="contact-item">
          <span class="contact-icon">
            <svg viewBox="0 0 16 16" aria-hidden="true"><path fill="#fff" d="M8 1.5a4.5 4.5 0 0 1 4.5 4.5C12.5 9.5 8 14.5 8 14.5S3.5 9.5 3.5 6A4.5 4.5 0 0 1 8 1.5z"/><circle cx="8" cy="6" r="1.8" fill="#e0353f"/></svg>
          </span>
          PO Box 587, Harlow Creek, VIC, 3942
        </li>
      </ul>
    </div>
  </section>
</body>
</html>
```